Business Card Design

I do estate sales and would like business card to reflect look and feel of attached logo. I also have copy of logo in .eps and .tif if you need that instead of .jpeg.
Updates

sorry for the delay in reviewing these designs. I will pick one by tomorrow. Here are the absolutes: *must have tagline (we find good homes for your treasures *must use blue and green *must be horizontal *nothing too fancy please submit your best and final. Thanks so much!

Industry/Entity Type

Business

Contact Information for Business Card

Nora Platt

DEALS by NORA
We find good homes for your treasures.

Specializing in one to three-day sales
o (no sale too big or too small)
• Home and garage organizing
• Home Clean-out

Call Nora Platt at 202-555-0187
to schedule.

```html
<!DOCTYPE html>
<html lang="en">
<head>
<meta charset="utf-8">
<title>DEALS by NORA – Business Card</title>
<link rel="stylesheet" href="https://fonts.googleapis.com/css2?family=Cabin:wght@500;600;700&display=swap">
<style>
  :root {
    --page-bg: #e9e6e1;
    --card-white: #fbfbf9;
    --stripe-grey: #dcdcdc;
    --logo-green: #7f9a5a;
    --panel-green-light: #b3c38f;
    --panel-green: #8ea366;
    --panel-green-deep: #6f8748;
    --panel-border: #ffffff;
    --text-white: #ffffff;
    --accent-blue: #2f9fd8;
    --text-dark: #3c4a2a;
  }
  * { margin: 0; padding: 0; box-sizing: border-box; }
  html, body {
    width: 1200px;
    height: 871px;
    overflow: hidden;
    background: var(--page-bg);
    font-family: "Cabin", Arial, sans-serif;
  }
  .business-card {
    position: absolute;
    left: 75px;
    top: 135px;
    width: 1050px;
    height: 600px;
    background: var(--card-white);
    box-shadow: 0 6px 24px rgba(0,0,0,0.18);
    overflow: hidden;
  }
  .stripe-band {
    position: absolute;
    left: 0;
    width: 100%;
    height: 70px;
    background: repeating-linear-gradient(
      to bottom,
      var(--stripe-grey) 0 2px,
      transparent 2px 7px
    );
    opacity: 0.7;
  }
  .stripe-band--top { top: 95px; }
  .stripe-band--bottom { top: 455px; }

  .brand-name {
    position: absolute;
    left: 40px;
    top: 175px;
    width: 400px;
    text-align: center;
    color: var(--logo-green);
    font-weight: 600;
    line-height: 1;
    background: var(--card-white);
    padding: 18px 0;
  }
  .brand-name__line { display: block; font-size: 96px; letter-spacing: 2px; }
  .brand-name__line--small { font-size: 46px; margin: 6px 0; }

  .info-panel {
    position: absolute;
    left: 470px;
    top: 40px;
    width: 550px;
    height: 500px;
    border-radius: 20px;
    border: 5px solid var(--panel-border);
    background: linear-gradient(to bottom, var(--panel-green-light) 0%, var(--panel-green) 55%, var(--panel-green-deep) 100%);
    box-shadow: 0 2px 8px rgba(0,0,0,0.2);
    color: var(--text-white);
    padding: 34px 36px;
  }
  .tagline {
    font-size: 25px;
    font-weight: 700;
    color: var(--text-dark);
    margin-bottom: 22px;
  }
  .services {
    list-style: none;
    font-size: 23px;
    font-weight: 600;
    color: var(--text-dark);
    line-height: 1.45;
  }
  .services li::before {
    content: "";
    display: inline-block;
    width: 9px; height: 9px;
    border-radius: 50%;
    background: var(--text-dark);
    margin: 0 12px 4px 6px;
  }
  .services__note { padding-left: 27px; font-weight: 500; font-size: 20px; }
  .services__note::before { display: none !important; }
  .call-to-action {
    margin-top: 30px;
    text-align: center;
    font-size: 34px;
    font-weight: 600;
    line-height: 1.25;
  }
  .call-to-action .highlight { color: var(--accent-blue); }
  .call-to-action .phone { font-size: 40px; font-weight: 700; }
  .signoff {
    position: absolute;
    left: 0; right: 0; bottom: 26px;
    text-align: center;
    font-size: 27px;
    font-weight: 700;
  }
</style>
</head>
<body>
  <div class="business-card">
    <div class="stripe-band stripe-band--top"></div>
    <div class="stripe-band stripe-band--bottom"></div>

    <div class="brand-name">
      <span class="brand-name__line">DEALS</span>
      <span class="brand-name__line brand-name__line--small">by</span>
      <span class="brand-name__line">NORA</span>
    </div>

    <div class="info-panel">
      <p class="tagline">We find good homes for your treasures.</p>
      <ul class="services">
        <li>Specializing in one to three-day sales</li>
        <li class="services__note">(no sale too big or too small)</li>
        <li>Home and garage organizing</li>
        <li>Home Clean-out</li>
      </ul>
      <p class="call-to-action">
        Call <span class="highlight">Nora Platt</span> at<br>
        <span class="highlight phone">202-555-0187</span><br>
        to schedule.
      </p>
      <p class="signoff">Nora Platt DEALS by NORA</p>
    </div>
  </div>
</body>
</html>
```